Colourful Bold Design for Pet Insurance Website

PLEASE NOTE THAT THIS PROJECT HAS BEEN EXTENDED. Please read the PROJECT EXTENSION DOCUMENT BEFORE STARTING WORK ON ANY DESIGNS.

We are looking for a colourful bold new template design for our JOOMLA HOMEPAGE and a matching design for our new WORDPRESS BLOG.

The website will help pet owners work out which insurance policy best meets their needs. The aim of the website is to explain policy differences in a plain clear manner.

The website will need to have a professional colourful image. It needs to be BOLD, CLEAN AND SHARP rather than soft, pastel and cuddly.

COLOUR SCHEME
The website needs to have a bold colourful design on a white background.
On the inner pages we will have five different types of policies which will be colour coded. We would ideally therefore like to incorporate five distinct colours in the design. See attached document for example of colour schemes we like.

LOGO
We want to keep the existing logo. Please find the file attached. You may though change the logo colours.

CONTENT
One of the reasons for the new design is that we want to change the style of the homepage and include new content. Our current homepage can be found at www.furrow-cover-polls.co.uk.

Content Required
Slideshow
Article Intro.. About Pet Insurance
Policy Lookup Box (see existing site… you can change the design of this)
Six link options (see links on left of current page)
Latest Reviews (List of 6)
Ad (Same dimensions as currently on homepage)

News and Comment Section - To include Three or Four Articles, Title, Intro to article (probably 3 or 4 lines .. about 400px wide), Read more link
Social Media Section
Friendwall Plugin with Feed
Latest Tweets Plugin
Pet Charities Latest Tweets
Footer
Larger footer with lots of links grouped in sections

It does not need to include the clipart pic of the pets which is on the current homepage.

Examples of Websites and Templates We Like
http://www.pawlane.com/ (like colours… fonts…layout)
http://sitetheme.brightkiln.com/?template=upbeat&path=/... (like the clarity, "white" space etc)
http://www.layoutforge.com/demo/51872.html (like white space, clear easy to read fonts… don’t like colour scheme, size of top picture)
http://www.layoutforge.com/website-templates/63915.html (like colour scheme, use of white space)

FEEDBACK
I will provide lots of feedback on all designs submitted so that together we can get the best result.

For clarification this is a DESIGN ONLY project. Our website developer will view the designs before we make our final choice as he wants to ensure he can develop "sharp, practical and most importantly light weight web interface" from the design.

Just updated this brief to clarify design issues, content issues and to give some more examples of site designs I like. 

Please note that although we wish to keep the logo you can change the colours to suit your design. 

Please note that we have now added details of pictures we would be happy to use on the website.  We would prefer it if you used one of these.   Otherwise please ensure your picture includes a nice dog and nice cat and no people!

I have been delighted with the quality of the designs submitted for this project.  So much so that I am going to extend the project to include some additional inner pages.   The amended brief will be posted on here on Friday 10 May.   The deadline will be extended and the budget will also be increased. 

Reason: Additional inner pages now required. Budget will be increased. Revised brief to be posted on here Friday 10 May.

Target Market(s)

Pet owners in the UK who are confused about pet insurance. It therefore needs to be a bold design which is plain, clean and easy to read. It should use bold colours rather than pastels and should not use "cuddly" images.

Industry/Entity Type

Insurance

Requirements
Must have
• Bold clear and distinct colours (preferably 5)
Content as per uploaded file (not just content from existing site)
Easy to read fonts
Should not have
• Pastel colours
Cuddly images

```html
<!DOCTYPE html>
<html lang="en">
<head>
<meta charset="utf-8">
<title>Furrow Cover Polls UK</title>
<link href="https://fonts.googleapis.com/css2?family=Open+Sans:wght@300;400;600&family=Arimo:wght@400;700&family=Noto+Serif:wght@700&display=swap" rel="stylesheet">
<style>
:root{
  --blue:#1a8ad6;
  --purple:#a050d8;
  --green:#6fcf87;
  --green-text:#4db06a;
  --orange:#f47b20;
  --orange-light:#f7931e;
  --ink:#1e1e1e;
  --footer:#ececec;
  --ad-blue:#0b5a9e;
  --ad-teal:#2ab8c0;
  --ad-yellow:#e8e84a;
}
*{box-sizing:border-box;margin:0;padding:0}
html,body{width:960px;height:1200px;overflow:hidden;background:#fff}
body{font-family:"Arimo",Arial,sans-serif;color:var(--ink)}
.page{position:relative;width:960px;height:1200px}
.abs{position:absolute}

/* header */
.brand{left:94px;top:36px;font-family:"Open Sans",sans-serif;font-weight:600;font-size:25px;line-height:25px;color:var(--blue);display:flex;align-items:center;gap:10px}
.brand-mark{width:34px;height:34px;background:var(--blue);flex:none}
.social{top:70px;width:26px;height:26px;border-radius:50%;background:var(--orange-light)}

/* nav */
.nav{left:0;top:122px;width:960px;height:41px;background:linear-gradient(#2eaaee,#1b86d2)}
.nav span{position:absolute;top:14px;color:#fff;font-size:11px;letter-spacing:.1px}

/* slider */
.slider{left:83px;top:173px;width:546px;height:266px;background:#fff;box-shadow:0 4px 6px rgba(0,0,0,.15);border:1px solid #f0f0f0}
.slider h2{position:absolute;left:25px;top:17px;font-family:"Open Sans",sans-serif;font-weight:400;font-size:15.4px;letter-spacing:-.2px;white-space:nowrap;color:var(--orange)}
.slider h2 b{font-weight:600;color:var(--green)}
.slide-photo{position:absolute;left:128px;top:56px;width:300px;height:206px;background:radial-gradient(ellipse at center,#d9cfc2 0%,#ece8e2 55%,#fff 80%)}
.slide-arrow{position:absolute;top:122px;width:21px;height:21px;border-radius:50%;background:#f2f2f2;border:1px solid #ccc}

/* policy lookup */
.lookup{left:636px;top:173px;width:242px;height:266px;background:#fafafa;box-shadow:0 4px 6px rgba(0,0,0,.15)}
.lookup-head{position:absolute;left:0;top:0;width:242px;height:34px;background:linear-gradient(#bd7cf0,#9a4cd8);color:#fff;font-family:"Open Sans",sans-serif;font-size:13px;line-height:34px;padding-left:55px}
.lookup-head svg{position:absolute;left:2px;top:2px}
.lookup label{position:absolute;left:12px;font-family:"Open Sans",sans-serif;font-size:12.5px;color:#555}
.select{position:absolute;left:10px;width:221px;height:32px;background:#fff;border:1px solid #ddd;font-size:10.5px;color:#666;line-height:30px;padding-left:10px}
.select i{position:absolute;right:6px;top:6px;width:18px;height:18px;border:1px solid #ddd}
.select i::after{content:"";position:absolute;left:5px;top:7px;border:4px solid transparent;border-top-color:#bbb}
.search-btn{position:absolute;left:36px;top:210px;width:171px;height:40px;border-radius:8px;background:linear-gradient(#c07cf2,#9848d6);color:#fff;font-family:"Noto Serif",serif;font-weight:700;font-size:18px;text-align:center;line-height:40px;letter-spacing:.5px}

/* welcome */
.welcome{left:82px;top:475px;width:506px}
.welcome h1{font-family:"Open Sans",sans-serif;font-weight:400;font-size:18px;letter-spacing:-.3px;color:var(--ink);padding-bottom:8px;border-bottom:1px solid #ccc}
.welcome h1 span{color:var(--blue)}
.welcome p{font-size:9.6px;line-height:14.4px;margin-top:12px;width:560px}
.welcome p.lead{font-weight:700;margin-top:14px}

/* ad */
.ad{left:638px;top:478px;width:240px;height:200px;background:var(--ad-blue);overflow:hidden;color:var(--ad-yellow);font-family:"Arimo",sans-serif}
.ad-art{position:absolute;left:0;top:0;width:96px;height:100px;background:linear-gradient(135deg,#5fd6dc,var(--ad-teal))}
.ad .tag{position:absolute;left:108px;top:34px;font-size:10px;font-weight:700;border-bottom:1px solid var(--ad-yellow);width:118px;padding-bottom:2px}
.ad .new{position:absolute;left:200px;top:57px;font-size:10px;font-weight:700}
.ad .name{position:absolute;left:128px;top:66px;font-size:22px;font-weight:700;color:#fff}
.ad .sub{position:absolute;left:134px;top:92px;font-size:9.5px;color:#fff}
.ad .visit{position:absolute;left:65px;top:129px;width:126px;height:24px;background:#fffde0;border:2px solid var(--ad-yellow);border-radius:4px;color:var(--ad-blue);font-size:8.5px;font-weight:700;text-align:center;line-height:20px}
.ad .call{position:absolute;left:31px;top:162px;font-size:10px;font-weight:700;line-height:14px}
.ad .call b{color:#fff;font-size:13px}

/* popular articles */
.articles{left:82px;top:612px;width:548px;height:234px;border:1px solid #eee;background:#fefdfd}
.band{position:absolute;left:0;top:0;height:33px;color:#fff;font-family:"Open Sans",sans-serif;font-size:13px;line-height:33px}
.articles .band{width:548px;background:linear-gradient(#7dd894,#62c67b);padding-left:20px}
.art-title{position:absolute;left:23px;font-size:9.5px;font-weight:700;color:var(--green-text)}
.tri{position:absolute;border:3px solid transparent;border-left:4px solid #555}
.art-body{position:absolute;left:22px;width:500px;font-size:9.5px;line-height:14.4px}
.more{position:absolute;right:30px;font-size:9.5px;font-weight:700}

/* section links */
.links{left:82px;top:862px;width:262px;height:203px;border:1px solid #e8e8e8}
.links a{position:absolute;left:27px;font-family:"Open Sans",sans-serif;font-size:13px;color:var(--blue);text-decoration:none}
.links a em{font-style:normal;color:var(--purple)}
.links .tri{left:15px}
.links hr{position:absolute;left:15px;width:223px;border:0;border-top:1px solid #ddd}

/* reviews */
.reviews{left:364px;top:862px;width:266px;height:203px;border:1px solid #eee}
.reviews .band{width:266px;background:linear-gradient(#f98f34,#f27420);padding-left:12px}
.reviews .band b{position:absolute;right:14px;font-family:"Arimo",sans-serif;font-size:9px}
.rev-title{position:absolute;left:21px;font-size:9.5px;font-weight:700;color:var(--orange);letter-spacing:.4px}
.rev-meta{position:absolute;left:22px;font-size:9.5px;color:#444}
.rev-body{position:absolute;left:20px;font-size:9.5px}
.stars{position:absolute;left:20px}
.reviews .more{right:5px}

/* friendwall plugin */
.fw{left:652px;top:693px;width:211px;height:225px;background:#333;border:1px solid #222;color:#fff;font-size:8px}
.fw-inner{position:absolute;left:8px;top:6px;width:195px;height:213px;border:1px solid #555}
.fw-head{position:absolute;left:3px;top:5px;font-weight:700;color:#ddd}
.fw-sq{position:absolute;width:32px;height:32px;background:#3b5a9a}
.fw-name{position:absolute;font-weight:700;font-size:8.5px}
.fw-like{position:absolute;left:54px;top:44px;width:30px;height:12px;background:#eee;border:1px solid #999;border-radius:2px}
.fw-post{position:absolute;left:5px;top:72px;width:186px;height:78px;border-top:1px solid #555;border-bottom:1px solid #555;overflow:hidden}
.fw-post p{position:absolute;left:48px;top:22px;width:128px;color:#aaa;font-size:7.5px;line-height:10.5px}
.fw-scroll{position:absolute;right:0;top:0;width:8px;height:78px;background:#fff}
.fw-count{position:absolute;left:5px;top:154px;color:#aaa;font-size:6.8px}
.fw-count b{color:#fff;font-weight:400}
.fw-faces{position:absolute;left:5px;top:166px;display:flex;gap:3px}
.fw-faces div{width:34px;height:32px}
.fw-foot{position:absolute;left:5px;top:200px;font-size:6.5px;color:#ddd;display:flex;align-items:center;gap:3px}
.fw-foot i{width:7px;height:7px;background:#3b5a9a}

/* chatterline feed */
.cl{left:652px;top:926px;width:213px;height:134px;background:#8dd6f7;border-radius:3px}
.cl .small{position:absolute;left:7px;top:6px;font-size:7px;color:#333}
.cl .title{position:absolute;left:7px;top:16px;font-family:"Open Sans",sans-serif;font-size:11.5px;color:#222}
.cl-feed{position:absolute;left:4px;top:36px;width:205px;height:74px;background:#fff;overflow:hidden}
.tweet{position:absolute;left:6px;width:185px;font-size:7.6px;line-height:10px;color:#444;padding-left:28px}
.tweet .av{position:absolute;left:0;top:2px;width:22px;height:22px}
.tweet b{color:#333}
.tweet small{display:block;font-size:6.5px;color:#555}
.cl-scroll{position:absolute;right:0;top:0;width:9px;height:74px;background:#e6eef8;border-left:1px solid #c7d4e6}
.cl-foot{position:absolute;left:7px;top:115px;width:199px;font-size:8.5px;font-weight:700;color:#222}
.cl-foot span:first-child{color:#fff}
.cl-foot span:last-child{position:absolute;right:0}

/* footer */
.footer{left:0;top:1074px;width:960px;height:126px;background:var(--footer)}
.footer a{position:absolute;font-size:9.6px;color:#222;text-decoration:none;padding-left:8px}
.footer a::before{content:"";position:absolute;left:0;top:3px;border:2.5px solid transparent;border-left:3.5px solid #444}
.footer-brand{position:absolute;left:666px;top:32px;font-family:"Open Sans",sans-serif;font-weight:600;font-size:20px;line-height:21px;color:#a9a9a9;display:flex;align-items:center;gap:8px}
.footer-brand i{width:28px;height:28px;background:#b5b5b5}
</style>
</head>
<body>
<div class="page">

  <svg width="0" height="0" style="position:absolute">
    <defs>
      <polygon id="star" points="8,0.8 10.2,5.6 15.3,6 11.4,9.4 12.6,14.5 8,11.8 3.4,14.5 4.6,9.4 0.7,6 5.8,5.6"/>
    </defs>
  </svg>

  <!-- header -->
  <div class="abs brand"><span class="brand-mark"></span><span>Furrow Cover<br>Polls UK</span></div>
  <div class="abs social" style="left:771px"></div>
  <div class="abs social" style="left:808px"></div>
  <div class="abs social" style="left:844px"></div>

  <nav class="abs nav">
    <span style="left:117px">HOME</span>
    <span style="left:179px">|</span>
    <span style="left:206px">POLICIES</span>
    <span style="left:287px">|</span>
    <span style="left:320px">GLOSSARY</span>
    <span style="left:416px">|</span>
    <span style="left:446px">FACT SHEETS</span>
    <span style="left:554px">|</span>
    <span style="left:585px">SURVEY REPORTS</span>
    <span style="left:709px">I</span>
    <span style="left:743px">NEWS &amp; COMMENT</span>
  </nav>

  <!-- slideshow -->
  <section class="abs slider">
    <h2>KNOW ABOUT <b>205 PET INSURANCE POLICIES</b> AVAILABLE IN THE UK</h2>
    <div class="slide-photo" role="img" aria-label="Photo of a dog, a spaniel, a kitten and two cats sitting together on white"></div>
    <div class="slide-arrow" style="left:13px"><svg width="19" height="19" viewBox="0 0 19 19"><path d="M11 5 L7 9.5 L11 14" fill="none" stroke="#333" stroke-width="2"/></svg></div>
    <div class="slide-arrow" style="left:511px"><svg width="19" height="19" viewBox="0 0 19 19"><path d="M8 5 L12 9.5 L8 14" fill="none" stroke="#333" stroke-width="2"/></svg></div>
  </section>

  <!-- policy lookup -->
  <section class="abs lookup">
    <div class="lookup-head">
      <svg width="50" height="46" viewBox="0 0 50 46"><line x1="14" y1="28" x2="4" y2="42" stroke="#333" stroke-width="4" stroke-linecap="round"/><circle cx="27" cy="16" r="13" fill="#c8f06a" stroke="#7a3bb0" stroke-width="3"/></svg>
      CHECK OUT A POLICY
    </div>
    <label style="top:60px">SELECT COMPNAPY</label>
    <div class="select" style="top:85px">Please select...<i></i></div>
    <label style="top:130px">SELECT POLICY</label>
    <div class="select" style="top:157px">Please select...<i></i></div>
    <div class="search-btn">SEARCH NOW</div>
  </section>

  <!-- welcome -->
  <section class="abs welcome">
    <h1>WELCOME TO <span>FURROW COVER POLLS UK</span></h1>
    <p class="lead">This is an independent website dedicated to helping you to find the best pet insurance policy for your pet</p>
    <p>Here you will find unbiased detailed information about almost all of the 205 pet insurance policies currently available in the UK<br>(we hope the other 3 will follow shortly!)<br>We do NOT sell any pet insurance policies nor do we receive commission from any insurance companies</p>
  </section>

  <!-- ad -->
  <aside class="abs ad">
    <div class="ad-art" role="img" aria-label="Advert artwork of teal arrow shapes"></div>
    <div class="tag">NOW AVAILABLE</div>
    <div class="new">NEW</div>
    <div class="name">NORVELA</div>
    <div class="sub">(veltaprin) tablets</div>
    <div class="visit">Visit www.NORVELA.com</div>
    <div class="call">or call toll-free at <b>1-877-555-0142</b><br>for more information.</div>
  </aside>

  <!-- popular articles -->
  <section class="abs articles">
    <div class="band">POPULAR ARTICLES</div>
    <span class="tri" style="left:14px;top:61px"></span>
    <div class="art-title" style="top:52px">Lorem Ipsum is simply dummy text</div>
    <div class="art-body" style="top:75px">pesetting industry. Lorem Ipsum has been the industry's standard dummy text ever ypesetting industry. Lorem Ipsum has been the industry's standard dummy text ever</div>
    <div class="more" style="top:104px">Read more...</div>

    <span class="tri" style="left:14px;top:114px"></span>
    <div class="art-title" style="top:114px">Lorem Ipsum is simply dummy text</div>
    <div class="art-body" style="top:133px">pesetting industry. Lorem Ipsum has been the industry's standard dummy text ever ypesetting industry. Lorem Ipsum has been the industry's standard dummy text ever</div>
    <div class="more" style="top:162px">Read more...</div>

    <span class="tri" style="left:14px;top:171px"></span>
    <div class="art-title" style="top:171px">Lorem Ipsum is simply dummy text</div>
    <div class="art-body" style="top:190px">pesetting industry. Lorem Ipsum has been the industry's standard dummy text ever ypesetting industry. Lorem Ipsum has been the industry's standard dummy text ever</div>
    <div class="more" style="top:219px">Read more...</div>
  </section>

  <!-- section links -->
  <nav class="abs links">
    <span class="tri" style="top:27px"></span><a style="top:18px">POLICY <em>FILES</em></a><hr style="top:37px">
    <span class="tri" style="top:56px"></span><a style="top:47px">POLICY <em>SEARCH</em></a><hr style="top:67px">
    <span class="tri" style="top:85px"></span><a style="top:76px">FACT <em>SHEETS</em></a><hr style="top:95px">
    <span class="tri" style="top:116px"></span><a style="top:107px">POLICY <em>LISTINGS BY TYPE</em></a><hr style="top:126px">
    <span class="tri" style="top:146px"></span><a style="top:137px"><em>CLAIMS SURVEY</em></a><hr style="top:157px">
    <span class="tri" style="top:177px"></span><a style="top:168px">2013 PRICE <em>SURVEY REPORT</em></a><hr style="top:190px">
  </nav>

  <!-- latest reviews -->
  <section class="abs reviews">
    <div class="band">LATEST REVIEWS<b>VIEW ALL</b></div>
    <span class="tri" style="left:9px;top:49px"></span>
    <div class="rev-title" style="top:46px">IOREM&nbsp; ISPUM</div>
    <div class="rev-meta" style="top:64px">By Ravi Mehta, 9 May 2013, 09:19 hrs IST</div>
    <div class="rev-body" style="top:84px">pesetting industry. Lorem Ipsum has been the industry's</div>
    <svg class="stars" style="top:101px" width="80" height="16" viewBox="0 0 80 16" fill="#f7a21b" stroke="#f7a21b">
      <use href="#star"/><use href="#star" x="16"/><use href="#star" x="32"/><use href="#star" x="48" fill="none"/><use href="#star" x="64" fill="none"/>
    </svg>
    <div class="more" style="top:104px">Read more..</div>

    <span class="tri" style="left:9px;top:127px"></span>
    <div class="rev-title" style="top:124px">IOREM&nbsp; ISPUM</div>
    <div class="rev-meta" style="top:142px">By Ravi Mehta, 9 May 2013, 09:19 hrs IST</div>
    <div class="rev-body" style="top:160px">pesetting industry. Lorem Ipsum has been the industry's</div>
    <svg class="stars" style="top:178px" width="80" height="16" viewBox="0 0 80 16" fill="#f7a21b" stroke="#f7a21b">
      <use href="#star"/><use href="#star" x="16"/><use href="#star" x="32"/><use href="#star" x="48" fill="none"/><use href="#star" x="64" fill="none"/>
    </svg>
    <div class="more" style="top:181px">Read more..</div>
  </section>

  <!-- friendwall plugin -->
  <aside class="abs fw">
    <div class="fw-inner">
      <div class="fw-head">Find us on Friendwall</div>
      <div class="fw-sq" style="left:5px;top:22px"></div>
      <div class="fw-name" style="left:42px;top:24px">Friendwall Developers</div>
      <div class="fw-like"></div>
      <div class="fw-post">
        <div class="fw-sq" style="left:2px;top:6px"></div>
        <div class="fw-name" style="left:48px;top:8px">Friendwall Developers</div>
        <p>Join us for a full-day build session in our London office to make tools more open and give people more control</p>
        <div class="fw-scroll"></div>
      </div>
      <div class="fw-count">1,474,964 people like <b>Friendwall Developers</b></div>
      <div class="fw-faces">
        <div style="background:#8fb9a8" role="img" aria-label="Profile photo of a fan"></div>
        <div style="background:#c9d3e6" role="img" aria-label="Profile photo of a fan"></div>
        <div style="background:#7a6a4a" role="img" aria-label="Profile photo of a fan"></div>
        <div style="background:#3a3a32" role="img" aria-label="Profile photo of a fan"></div>
        <div style="background:#8a8f98" role="img" aria-label="Profile photo of a fan"></div>
      </div>
      <div class="fw-foot"><i></i>Friendwall social plugin</div>
    </div>
  </aside>

  <!-- chatterline feed -->
  <aside class="abs cl">
    <div class="small">Chatterline feed</div>
    <div class="title">Evening Courier</div>
    <div class="cl-feed">
      <div class="tweet" style="top:5px"><div class="av" style="background:#f2d9b0" role="img" aria-label="Account avatar"></div><b>CourierPreview</b> 'The voice of the voiceless' <b>http://cour.ly/Hx3bQ9</b><small>43 minutes ago</small></div>
      <div class="tweet" style="top:42px"><div class="av" style="background:#b8a58e" role="img" aria-label="Account avatar"></div><b>marcobellin</b> Chatterline news: Harbour council plans a new park; local updates about the dangers of flooding</div>
      <div class="cl-scroll"></div>
    </div>
    <div class="cl-foot"><span>chatterline</span><span>Join the conversation</span></div>
  </aside>

  <!-- footer -->
  <footer class="abs footer">
    <a style="left:84px;top:24px">Example link</a>
    <a style="left:84px;top:43px">Example link</a>
    <a style="left:84px;top:60px">Example link</a>
    <a style="left:84px;top:77px">Example link</a>
    <a style="left:84px;top:96px">Example link</a>

    <a style="left:220px;top:23px">Example link</a>
    <a style="left:220px;top:41px">Example link</a>
    <a style="left:220px;top:59px">Example link</a>
    <a style="left:220px;top:77px">Example link</a>
    <a style="left:220px;top:94px">Example link</a>

    <a style="left:344px;top:26px">Example link</a>
    <a style="left:344px;top:43px">Example link</a>
    <a style="left:344px;top:60px">Example link</a>
    <a style="left:344px;top:78px">Example link</a>
    <a style="left:342px;top:95px">Example link</a>

    <a style="left:481px;top:26px">Example link</a>
    <a style="left:481px;top:43px">Example link</a>
    <a style="left:481px;top:60px">Example link</a>
    <a style="left:481px;top:77px">Example link</a>
    <a style="left:481px;top:94px">Example link</a>

    <div class="footer-brand"><i></i><span>Furrow Cover<br>Polls UK</span></div>
  </footer>

</div>
</body>
</html>
```